Theo Brandvik Photography
Theo Brandvik Photography's Homepage
Photography
Professional photographer
top
Overall look and feel should come from logo design.

```html
<!DOCTYPE html>
<html lang="en">
<head>
<meta charset="utf-8">
<title>Theo Brandvik Photography</title>
<link href="https://fonts.googleapis.com/css2?family=Arimo:wght@400;700&family=Kalam:wght@400;700&display=swap" rel="stylesheet">
<style>
:root{
  --black:#070707;
  --coal:#141414;
  --panel:#1c1c1c;
  --grey:#8a8a8a;
  --light:#d8d8d8;
  --white:#f4f4f4;
  --yellow:#f2d100;
  --yellow-deep:#c9a800;
  --field:#e9e9e9;
}
*{box-sizing:border-box;margin:0;padding:0}
html,body{width:1200px;height:1014px;overflow:hidden;background:var(--black)}
body{position:relative;font-family:Arimo,Arial,sans-serif;color:var(--light);
  background:radial-gradient(ellipse at 50% 55%,#2a2a2a 0%,#151515 45%,#050505 100%)}
.header-band{position:absolute;left:0;top:0;width:1200px;height:165px;background:linear-gradient(#0b0b0b,#1a1a1a)}
.brand{position:absolute;left:250px;top:16px;display:flex;align-items:center;gap:10px}
.brand-mark{width:34px;height:34px;background:var(--white)}
.brand-name{font-weight:700;font-size:22px;color:var(--white);line-height:1}
.site-search{position:absolute;left:850px;top:22px;display:flex;align-items:center;gap:8px;font-size:12px;color:var(--grey)}
.site-search span{width:110px;height:18px;background:var(--field);border:1px solid #555}
.main-nav{position:absolute;left:520px;top:50px;width:425px;height:27px;background:linear-gradient(var(--yellow),var(--yellow-deep));display:flex;justify-content:space-around;align-items:center;font-size:11px;font-weight:700;color:var(--white);text-transform:uppercase}
.hero-frame{position:absolute;left:150px;top:77px;width:890px;height:246px;background:#e8e8e8;padding:10px 22px}
.hero-photo{width:100%;height:100%;background:linear-gradient(180deg,#a9c6d6 0%,#6f9a5c 45%,#3f6a2c 75%,#1f3214 100%)}
.hero-title{position:absolute;left:252px;top:232px;font-family:Kalam,cursive;font-weight:700;font-size:29px;color:var(--white);text-shadow:0 2px 3px #000}
.hero-sub{position:absolute;left:365px;top:270px;font-family:Kalam,cursive;font-weight:700;font-size:27px;color:var(--yellow);text-shadow:0 2px 3px #000}
.rule{position:absolute;left:0;width:1200px;height:9px;background:var(--yellow)}
.rule.top{top:335px}
.rule.bottom{top:956px}
.intro{position:absolute;left:220px;top:384px;width:535px}
.intro h1{font-family:Kalam,cursive;font-size:19px;font-weight:700;color:var(--white);margin-bottom:14px}
.intro p{font-size:10.5px;line-height:15px;color:var(--grey);margin-bottom:14px}
.sidebar{position:absolute;left:780px;top:380px;width:205px}
.sidebar h2{font-family:Kalam,cursive;font-size:17px;font-weight:700;color:var(--white);margin-bottom:8px}
.finder{background:var(--panel);padding:10px 10px 12px}
.finder-row{display:flex;justify-content:space-between;align-items:center;height:26px;font-size:10px;color:var(--light)}
.finder-row span{width:92px;height:17px;background:var(--field);position:relative}
.finder-row span::after{content:"";position:absolute;right:0;top:0;width:15px;height:17px;background:#333}
.finder-button{margin:8px 0 0 auto;width:56px;height:20px;background:#444;color:var(--white);font-size:10px;display:flex;align-items:center;justify-content:center}
.social{margin-top:14px}
.social-badge{display:block;width:110px;height:42px;margin:14px auto 0;background:#cfcfcf;color:#333;font-weight:700;font-size:17px;display:flex;align-items:center;justify-content:center}
.featured-label{position:absolute;left:262px;top:846px;font-family:Kalam,cursive;font-weight:700;font-size:17px;color:var(--yellow)}
.film-strip{position:absolute;left:241px;top:872px;width:767px;height:78px;background:#eeeeee;display:flex;justify-content:space-around;align-items:center;padding:0 22px}
.thumb{width:88px;height:62px;background:linear-gradient(#c8c8c8,#8d8d8d);border:3px solid #fff}
.footer-note{position:absolute;left:0;top:972px;width:1200px;text-align:center;font-size:11px;color:var(--light)}
</style>
</head>
<body>
<div class="header-band"></div>
<div class="brand"><span class="brand-mark"></span><span class="brand-name">Theo Brandvik Photography</span></div>
<div class="site-search">Search: <span></span></div>
<nav class="main-nav"><a>Home</a><a>About</a><a>Portfolio</a><a>Clients Area</a><a>Links</a><a>Contact</a></nav>

<div class="hero-frame"><div class="hero-photo" role="img" aria-label="Photographer standing on a hilltop above green valleys"></div></div>
<div class="hero-title">Sed placerat mollis lorem eu malesuada</div>
<div class="hero-sub">Cras tempus, orci placerat ultricies</div>
<div class="rule top"></div>

<section class="intro">
  <h1>Welcome to Theo Brandvik Photography</h1>
  <p>Lorem ipsum dolor sit amet, consectetur adipiscing elit. Sed placerat mollis lorem eu malesuada. Cras tempus orci placerat ultricies tincidunt, nulla magna aliquet nisi, quis vehicula augue lorem at mauris. Integer euismod volutpat justo, vitae faucibus ligula dignissim in. Curabitur feugiat, sapien in tempor accumsan, lectus massa viverra orci, non porta nibh mi sed lacus. Aliquam erat volutpat. Vestibulum ante ipsum primis in faucibus orci luctus et ultrices posuere cubilia.</p>
  <p>Donec sed velit at turpis interdum aliquam. Phasellus vitae tortor eget arcu pulvinar ornare. Nullam blandit, enim non luctus faucibus, erat felis dictum justo, et consequat nisl urna nec erat. Mauris varius dolor eu lectus sodales, quis rhoncus lorem feugiat. Pellentesque habitant morbi tristique senectus et netus et malesuada fames ac turpis egestas. Morbi ultrices nibh sed tellus lacinia, at tempus sem luctus. Proin gravida neque id tortor commodo finibus.</p>
  <p>Fusce dictum ante vitae sem finibus, a posuere mi faucibus. Quisque lacinia diam vel tellus pretium, sed bibendum quam sodales. Etiam vel ipsum non nisl tincidunt porta. Nunc fermentum leo in diam facilisis, a pellentesque odio convallis. Aenean at placerat nibh.</p>
</section>

<aside class="sidebar">
  <h2>Search</h2>
  <div class="finder">
    <div class="finder-row">From <span></span></div>
    <div class="finder-row">Near <span></span></div>
    <div class="finder-row">Who's good at <span></span></div>
    <div class="finder-row">Shooting on <span></span></div>
    <div class="finder-row">Lighting with <span></span></div>
    <div class="finder-row">And can use <span></span></div>
    <div class="finder-button">Search</div>
  </div>
  <div class="social">
    <h2>Find us on</h2>
    <a class="social-badge">Chirpline</a>
    <a class="social-badge">Friendloop</a>
  </div>
</aside>

<div class="featured-label">Featured pictures</div>
<div class="film-strip">
  <div class="thumb" role="img" aria-label="Featured portrait"></div>
  <div class="thumb" role="img" aria-label="Featured portrait"></div>
  <div class="thumb" role="img" aria-label="Featured portrait"></div>
  <div class="thumb" role="img" aria-label="Featured portrait"></div>
  <div class="thumb" role="img" aria-label="Featured portrait"></div>
  <div class="thumb" role="img" aria-label="Featured portrait"></div>
  <div class="thumb" role="img" aria-label="Featured portrait"></div>
</div>
<div class="rule bottom"></div>
<footer class="footer-note">© 2010 Theo Brandvik Photography All Rights Reserved.</footer>
</body>
</html>
```